Innovative Consulting Firm Needs New Business Cards and Stationary

Our Innovative Consulting Firm, Larkfield Consulting, is in need of new business cards and stationary designs. We want two-sided cards that incorporate our logo, which is attached. We are looking for something not too formal, but is professional and slick.

Card should have the following information:
Name (ex. Tom Bradley)
Title (ex. Manager)
Address (ex. 24680 Cedar Lane)
Address 2 (ex. Suite 100)
City
State
Zip Code
Mobile
Email

The card should also have our website: www.larkfieldconsulting.example

Industry/Entity Type

Management Consulting

Contact Information for Business Card

Name (ex. Tom Bradley)
Title (ex. Manager)
Address 2 (ex. Suite 100)
City
State
Zip Code
Mobile
Email

Font styles to use
Sans Serif

Requirements
Must have
• The colors on the card must match the colors in the logo. The exact color codes are attached in a pdf.
Nice to have
• The Company's Tagline is "Clear Paths to Growth". This might be nice to incorporate, but not necessary.

```html
<!DOCTYPE html>
<html lang="en">
<head>
<meta charset="utf-8">
<title>Larkfield Consulting – Business Card</title>
<link rel="stylesheet" href="https://fonts.googleapis.com/css2?family=PT+Sans:ital,wght@0,400;0,700;1,700&display=swap">
<style>
  :root {
    --backdrop-top: #262626;
    --backdrop-bottom: #050505;
    --card-white: #ffffff;
    --navy: #1d4576;
    --ink: #1a1a1a;
    --gold: #f0a81c;
    --card-blue: #21507e;
    --card-blue-text: #7fb0e0;
  }
  html, body {
    margin: 0;
    width: 1200px;
    height: 900px;
    overflow: hidden;
  }
  body {
    position: relative;
    background: linear-gradient(180deg, var(--backdrop-top) 0%, #141414 55%, var(--backdrop-bottom) 100%);
    font-family: "PT Sans", Arial, sans-serif;
  }
  .card {
    position: absolute;
    top: 306px;
    width: 439px;
    height: 271px;
    border-radius: 12px;
    overflow: hidden;
  }
  .card--front { left: 149px; background: var(--card-white); }
  .card--back  { left: 608px; background: var(--card-blue); }

  .wordmark {
    position: absolute;
    left: 0;
    width: 100%;
    text-align: center;
    margin: 0;
    font-weight: 400;
    font-size: 36px;
    line-height: 1;
    letter-spacing: 0.5px;
  }
  .card--front .wordmark { top: 44px; color: var(--navy); }
  .card--back .wordmark  { top: 116px; color: var(--card-blue-text); }

  .person {
    position: absolute;
    right: 231px;
    top: 128px;
    text-align: right;
    color: var(--ink);
    font-size: 13px;
    line-height: 15px;
  }
  .person__name {
    margin: 0;
    font-size: 18px;
    line-height: 20px;
    font-weight: 700;
    color: var(--navy);
  }
  .person__title { margin: 0 0 4px; line-height: 14px; }
  .person__address { margin: 0; font-style: normal; }

  .divider {
    position: absolute;
    left: 220px;
    top: 129px;
    width: 1px;
    height: 67px;
    background: var(--gold);
  }

  .contact {
    position: absolute;
    left: 229px;
    top: 140px;
    margin: 0;
    padding: 0;
    list-style: none;
    font-size: 13px;
    line-height: 15.5px;
    color: var(--ink);
  }
  .contact li { display: flex; align-items: center; gap: 4px; }
  .contact svg { width: 9px; height: 9px; fill: var(--navy); flex: none; }

  .tagline {
    position: absolute;
    left: 0;
    top: 222px;
    width: 100%;
    text-align: center;
    margin: 0;
    font-size: 13px;
    line-height: 16px;
    font-weight: 700;
    font-style: italic;
    color: var(--navy);
  }
</style>
</head>
<body>
  <section class="card card--front" aria-label="Business card front">
    <h1 class="wordmark">Larkfield Consulting</h1>

    <div class="person">
      <h2 class="person__name">Tom Bradley</h2>
      <p class="person__title">Manager</p>
      <address class="person__address">24680 Cedar Lane Suite<br>CityState, Zip Code</address>
    </div>

    <span class="divider" aria-hidden="true"></span>

    <ul class="contact">
      <li>
        <svg viewBox="0 0 10 10" aria-hidden="true"><path d="M1 3c0-1 1-2 4-2s4 1 4 2v1H7V3H3v1H1zM2 5h6l1 4H1z"/></svg>
        044-555 010 234
      </li>
      <li>
        <svg viewBox="0 0 10 10" aria-hidden="true"><rect x="0.5" y="2" width="9" height="6.5"/><path d="M0.5 2l4.5 3.5L9.5 2" fill="none" stroke="#fff" stroke-width="0.9"/></svg>
        info@larkfield.example
      </li>
      <li>
        <svg viewBox="0 0 10 10" aria-hidden="true"><circle cx="5" cy="5" r="4.5"/></svg>
        www.larkfieldconsulting.example
      </li>
    </ul>

    <p class="tagline">Clear Paths to Growth</p>
  </section>

  <section class="card card--back" aria-label="Business card back">
    <p class="wordmark">Larkfield Consulting</p>
  </section>
</body>
</html>
```